VELRO - Business cards

Business card to be created for Commercial sales staff

Target Market(s)

Commercial businesses

Industry/Entity Type

Commercial

Contact Information for Business Card

Look professional. For commercial clients

Colors
ffffff

Requirements
Must have
• - Velro Logo
• - Commercial sales staff as postion
• - room for commerical sales manager role
• - person name and their mobile number
• - Website : velropower.com.au
Nice to have
• White background.
• On back of business card just have the logo no other information
Should not have
• Should only have white background on front of card.

```html
<!DOCTYPE html>
<html lang="en">
<head>
<meta charset="UTF-8">
<title>Velro – Business Cards</title>
<link rel="stylesheet" href="https://fonts.googleapis.com/css2?family=Roboto:wght@400;700;900&display=swap">
<style>
  :root {
    --stage: #2b2b2d;
    --card-dark: #2d3038;
    --card-dark-edge: #3a3e48;
    --brand-red: #d3202b;
    --brand-red-deep: #a8141d;
    --ink: #2a2d33;
    --white: #ffffff;
    --muted: #d9dbe0;
  }
  * { box-sizing: border-box; margin: 0; padding: 0; }
  html, body { width: 1200px; height: 950px; overflow: hidden; }
  body {
    background: var(--stage);
    font-family: "Roboto", Arial, sans-serif;
    position: relative;
  }
  .card {
    position: absolute;
    width: 580px;
    height: 332px;
    border-radius: 4px;
    overflow: hidden;
  }
  /* Front card: dark contact side */
  .card--contact {
    left: 90px;
    top: 120px;
    background: linear-gradient(135deg, var(--card-dark-edge), var(--card-dark) 60%);
  }
  .card__artwork {
    position: absolute;
    left: 0; top: 0;
    width: 270px; height: 100%;
    background: linear-gradient(160deg, var(--brand-red) 0%, var(--brand-red-deep) 40%, var(--white) 75%);
    clip-path: polygon(0 0, 70% 0, 100% 45%, 80% 100%, 0 100%);
  }
  .contact {
    position: absolute;
    right: 36px;
    top: 34px;
    text-align: right;
    color: var(--white);
  }
  .contact__name {
    color: var(--brand-red);
    font-size: 22px;
    font-weight: 400;
    margin-bottom: 4px;
  }
  .contact__role {
    font-size: 15px;
    color: var(--muted);
    margin-bottom: 16px;
  }
  .contact__line {
    display: flex;
    justify-content: flex-end;
    align-items: center;
    gap: 8px;
    font-size: 13px;
    color: var(--muted);
    line-height: 22px;
  }
  .contact__line svg { width: 12px; height: 12px; fill: var(--brand-red); }
  .contact__web { font-size: 13px; color: var(--muted); line-height: 22px; }
  .wordmark {
    font-family: "Roboto", Arial, sans-serif;
    font-weight: 900;
    letter-spacing: 1px;
  }
  .card--contact .wordmark {
    position: absolute;
    right: 36px;
    bottom: 30px;
    font-size: 56px;
    color: var(--white);
  }
  /* Back card: white logo side */
  .card--logo {
    left: 530px;
    top: 500px;
    background: var(--white);
    display: flex;
    align-items: center;
    justify-content: center;
    gap: 16px;
  }
  .card--logo .mark-dot {
    width: 34px; height: 34px;
    border-radius: 50%;
    background: var(--brand-red);
  }
  .card--logo .wordmark {
    font-size: 72px;
    color: var(--ink);
  }
</style>
</head>
<body>
  <section class="card card--contact" aria-label="Business card, contact side">
    <div class="card__artwork" role="img" aria-label="Large red and white brand illustration"></div>
    <div class="contact">
      <p class="contact__name">Alan Merrow</p>
      <p class="contact__role">Manager, Commercial Sales</p>
      <p class="contact__line">512 7304 8816
        <svg viewBox="0 0 12 12" aria-hidden="true"><path d="M2 1h3l1 3-1.5 1a6 6 0 0 0 2.5 2.5L8 6l3 1v3a1 1 0 0 1-1 1A9 9 0 0 1 1 2a1 1 0 0 1 1-1z"/></svg>
      </p>
      <p class="contact__line">845 2019 6637
        <svg viewBox="0 0 12 12" aria-hidden="true"><path d="M3 0h6a1 1 0 0 1 1 1v10a1 1 0 0 1-1 1H3a1 1 0 0 1-1-1V1a1 1 0 0 1 1-1zm0 2v7h6V2z"/></svg>
      </p>
      <p class="contact__line">alan@velropower.com.au
        <svg viewBox="0 0 12 12" aria-hidden="true"><path d="M0 2h12v8H0zm1 1v.5l5 3 5-3V3z"/></svg>
      </p>
      <p class="contact__line">velropower.com.au
        <svg viewBox="0 0 12 12" aria-hidden="true"><circle cx="6" cy="6" r="5.5"/></svg>
      </p>
    </div>
    <p class="wordmark">VELRO</p>
  </section>

  <section class="card card--logo" aria-label="Business card, logo side">
    <span class="mark-dot" aria-hidden="true"></span>
    <p class="wordmark">VELRO</p>
  </section>
</body>
</html>
```